依頼詳細
トップページのデザイン トップページとサブページ(2ページ目以降)のデザイン サブページは、トップページのデザインを引き継ぐ感じで
グローバルナビ  ワードプレス×レスポンシブで制作予定

全体的なイメージ https://www.morino-kobo.jp/index.html
青とホワイトを基調にした清潔感があり ごちゃごちゃしすぎず
患者さんの視線で見やすく 探しやすい感じを希望します。
お子様や女性にも好まれるような可愛いイラストなどもお願いします。

グローバルナビに入れる予定の項目 Q&A、アクセス、医院紹介、治療内容、マウスピース矯正、費用、部分矯正、裏側矯正

トップページに記載したい文章
マウスピース型矯正装置(クリアフィット)をメインの紹介するサイト
裏側矯正にも力入れており、見えないMIX (マウスピース矯正と裏側矯正の組み合わせで幅広く対応できる。

最新式 デジタルスキャナー dento scope の紹介
参考https://hanawa-dent.jp/orthodontic/clearfit/

ブログ形式で 新着情報
休診日・診療時間/
ご相談・お問い合わせ

希望イメージ
シンプル 複雑
単色 カラフル
暗い 明るい
日常 高級
遊び心 厳粛
未来的 伝統的
女性的 男性的
希望する色
水色系
納品ファイル
• 高解像度JPG (.jpg)
• フォトショップ形式 (.psd)
補足説明
マウスピース矯正を マウスピース型矯正装置
クリアフィット をマウスピース型矯正装置(クリアフィット)

※医療広告の関係で表記を統一してください。
用語は、マウスピース型矯正装置(クリアフィット)を徹底してください。

高校生~20代女性に響くような デザインが希望です。

透明で見ないこと 取り外せること
最新式 3Dスキャンナー dento scoopeを導入していること
dento scope により、簡易シュミレーションが見れること
裏側矯正も得意なことから 組み合わせることによって対応できる
幅が広がったこと。

を強調したデザインが希望です。

参照https://www.kirari-ha.jp/simulation/

なるべく裏側矯正の内容は、記載しないでマウスピース型矯正装置(クリアフィット)の内容だけにしたい。

よろしくお願いします。

```html
<!DOCTYPE html>
<html lang="ja">
<head>
<meta charset="utf-8">
<title>花輪町クリア矯正歯科</title>
<link href="https://fonts.googleapis.com/css2?family=Noto+Sans+JP:wght@400;500;700;900&family=Montserrat:wght@600;700&display=swap" rel="stylesheet">
<style>
:root{
  --blue:#1e9be6;
  --blue-dark:#1380c8;
  --sky:#cfe8f8;
  --pale:#e9f5fc;
  --white:#ffffff;
  --text:#333d47;
  --muted:#8a99a6;
  --dot:#f08a5d;
}
*{margin:0;padding:0;box-sizing:border-box}
html,body{width:1200px;height:4964px;overflow:hidden}
body{position:relative;background:var(--white);font-family:"Noto Sans JP",sans-serif;color:var(--text)}
.abs{position:absolute}
.btn{position:absolute;display:flex;align-items:center;justify-content:center;background:var(--blue);color:#fff;border-radius:20px;font-size:12px;font-weight:700;height:34px;width:160px}
.heading{position:absolute;left:0;width:1200px;text-align:center;color:var(--blue);font-weight:700}
.body-text{font-size:13px;line-height:1.9;color:var(--text)}

/* header */
.header{position:absolute;top:0;left:0;width:1200px;height:90px;z-index:3}
.logo{position:absolute;left:40px;top:22px;display:flex;align-items:center;gap:10px}
.logo-mark{width:34px;height:34px;border-radius:50%;background:var(--blue)}
.logo small{display:block;font-size:10px;color:var(--muted)}
.logo strong{display:block;font-size:17px;color:var(--blue);font-weight:700}
.nav{position:absolute;left:470px;top:46px;display:flex;gap:0;font-size:12px;color:var(--text);font-weight:500}
.nav span{padding:0 14px;border-left:1px solid #c7d3dc}
.nav span:first-child{border-left:none}
.tel{position:absolute;right:40px;top:22px;text-align:right;color:var(--blue)}
.tel small{display:block;font-size:10px;color:var(--muted)}
.tel strong{font-family:"Montserrat",sans-serif;font-size:28px;font-weight:700;display:flex;align-items:center;gap:8px}

/* hero */
.hero-photo{position:absolute;top:0;left:0;width:1200px;height:780px;background:linear-gradient(180deg,#f2f1ef 0%,#ece5df 40%,#dfeaf3 75%,#cfe6f6 100%)}
.hero-copy{position:absolute;left:120px;top:540px;color:var(--blue);font-size:44px;font-weight:700;line-height:1.4}

/* treatment */
.treat-cards{position:absolute;top:920px;left:280px;display:flex;gap:44px}
.card{width:180px;height:170px;background:#fff;box-shadow:0 4px 16px rgba(30,120,200,.15);text-align:center;padding-top:42px;position:relative}
.card h3{font-size:17px;font-weight:700}
.card p{font-size:10px;color:var(--muted);margin-top:6px}
.card .btn{left:25px;top:112px;width:130px;height:28px;font-size:10px}

/* news */
.news{position:absolute;left:140px;top:1380px;width:440px}
.news-title{font-family:"Montserrat",sans-serif;color:var(--blue);font-size:34px;font-weight:700;border-left:6px solid var(--blue);padding-left:10px;line-height:1}
.news-item{margin-top:18px;font-size:11px;color:var(--muted)}
.news-item p{color:var(--text);margin-top:3px}
.schedule{position:absolute;left:652px;top:1372px;width:396px;border-collapse:collapse;font-size:11px;text-align:center}
.schedule th{background:var(--blue);color:#fff;height:36px;font-weight:500}
.schedule td{height:50px;border-bottom:1px solid #cde3f2;color:var(--blue)}
.schedule .time{width:96px;font-weight:500}
.dot{display:inline-block;width:14px;height:14px;border-radius:50%;background:var(--dot)}

/* points */
.point{position:absolute;display:flex;align-items:center;gap:16px;font-size:18px;font-weight:500}
.point b{display:inline-block;width:110px;height:32px;line-height:32px;background:#7cc2ee;color:#fff;font-family:"Montserrat",sans-serif;font-size:13px;text-align:center}

/* flow */
.flow{position:absolute;top:4170px;left:130px;display:flex;gap:60px}
.step{width:190px;text-align:center}
.step svg{display:block;margin:0 auto 8px}
.step h4{color:var(--blue);font-size:12px;font-weight:700}
.step p{font-size:10px;color:var(--muted);margin-top:4px;line-height:1.7}

/* footer */
.footer{position:absolute;left:0;top:4790px;width:1200px;height:174px;background:var(--blue);color:#fff}
</style>
</head>
<body>

<!-- hero -->
<div class="hero-photo" role="img" aria-label="白い歯で微笑む女性の口元のクローズアップ写真"></div>
<header class="header">
  <div class="logo"><span class="logo-mark"></span><div><small>歯並びの専門医による矯正歯科</small><strong>花輪町クリア矯正歯科</strong></div></div>
  <nav class="nav"><span>HOME</span><span>治療内容</span><span>費用</span><span>医院紹介</span><span>Q&amp;A</span><span>アクセス</span></nav>
  <div class="tel"><small>お電話でのご予約</small><strong><svg width="24" height="24" viewBox="0 0 24 24"><circle cx="12" cy="12" r="11" fill="none" stroke="#1e9be6" stroke-width="2"/><path d="M8 7l2 0 1 3-1.5 1a6 6 0 0 0 3 3l1-1.5 3 1v2c-5 1-10-4-9-9z" fill="#1e9be6"/></svg>03-0000-0000</strong></div>
</header>
<h1 class="hero-copy">心からの笑顔が<br>あなたを美しく魅せる</h1>

<!-- soft wave backgrounds -->
<svg class="abs" style="left:0;top:700px" width="1200" height="4100" viewBox="0 0 1200 4100">
  <path d="M0 80 Q300 30 600 110 T1200 60 V300 Q900 380 600 330 T0 340Z" fill="#e9f5fc"/>
  <circle cx="1260" cy="250" r="230" fill="#d6ecfa"/>
  <circle cx="-60" cy="330" r="140" fill="#d6ecfa"/>
  <path d="M0 860 Q200 760 420 790 Q720 830 1200 700 V1000 Q900 1050 600 1000 Q300 950 0 1040Z" fill="#d6ecfa"/>
  <circle cx="600" cy="2000" r="760" fill="#d6ecfa"/>
  <circle cx="1150" cy="2250" r="320" fill="#e9f5fc"/>
  <path d="M0 3150 Q200 3000 430 3100 Q700 3220 1200 3050 V3640 H0Z" fill="#d6ecfa"/>
  <rect x="0" y="3640" width="1200" height="460" fill="#d6ecfa"/>
</svg>

<!-- treatment menu -->
<h2 class="heading" style="top:860px;font-size:24px">診療内容</h2>
<div class="abs" style="left:560px;top:900px;width:80px;height:2px;background:var(--blue)"></div>
<div class="treat-cards">
  <div class="card"><h3>マウスピース矯正</h3><p>テキストテキスト</p><span class="btn">詳細を見る</span></div>
  <div class="card"><h3>部分矯正</h3><p>テキストテキスト</p><span class="btn">詳細を見る</span></div>
  <div class="card"><h3>裏側矯正</h3><p>テキストテキスト</p><span class="btn">詳細を見る</span></div>
</div>

<!-- news & schedule -->
<section class="news">
  <div class="news-title">NEWS</div>
  <div class="news-item">2018.01.01<p>休診日のお知らせと年末年始の診療時間について</p></div>
  <div class="news-item">2018.01.01<p>無料相談会を開催いたします</p></div>
</section>
<table class="schedule">
  <tr><th class="time">診療時間</th><th>月</th><th>火</th><th>水</th><th>木</th><th>金</th><th>土</th><th>日</th></tr>
  <tr><td class="time">9:00~12:00</td><td><span class="dot"></span></td><td><span class="dot"></span></td><td><span class="dot"></span></td><td><span class="dot"></span></td><td><span class="dot"></span></td><td><span class="dot"></span></td><td>/</td></tr>
  <tr><td class="time">13:00~21:00</td><td><span class="dot"></span></td><td><span class="dot"></span></td><td><span class="dot"></span></td><td><span class="dot"></span></td><td><span class="dot"></span></td><td><span class="dot"></span></td><td>/</td></tr>
</table>

<!-- recommended -->
<h2 class="heading" style="top:1520px;font-size:40px;font-weight:900">当院のおすすめ診療</h2>
<h3 class="heading" style="top:1680px;font-size:26px">マウスピース矯正</h3>
<p class="heading" style="top:1730px;font-size:17px;line-height:1.6;color:#5db5ec">誰にも気付かれずに歯並びを治したい方に<br>透明で見えないマウスピース矯正</p>
<div class="abs" role="img" aria-label="手鏡で歯並びを確認する女性の写真" style="left:180px;top:1960px;width:390px;height:300px;background:linear-gradient(135deg,#f4f6f8,#dfe7ee)"></div>
<p class="abs body-text" style="left:640px;top:2010px;width:420px">マウスピース型矯正装置は透明で目立たず、食事や歯みがきの時には取り外すことができます。装置による痛みや違和感も少なく、通院の回数も抑えられるため、学校やお仕事が忙しい方にも続けやすい矯正方法です。まずはお気軽にご相談ください。</p>
<span class="btn" style="left:930px;top:2150px">詳細を見る</span>

<!-- clear fit -->
<h3 class="heading" style="top:2410px;font-size:26px">クリアフィット</h3>
<p class="heading" style="top:2460px;font-size:17px;line-height:1.6;color:#5db5ec">今までのワイヤーを使った矯正治療とは異なり<br>透明なマウスピースを使った矯正方法</p>
<div class="point" style="left:220px;top:2580px"><b>POINT 1</b>透明で目立たない</div>
<div class="point" style="left:220px;top:2640px"><b>POINT 2</b>取り外しが可能</div>
<div class="point" style="left:220px;top:2700px"><b>POINT 3</b>痛みが少ない</div>
<div class="point" style="left:600px;top:2580px"><b>POINT 4</b>自分で取り外しが可能</div>
<div class="point" style="left:600px;top:2640px"><b>POINT 5</b>通院回数が少ない</div>
<span class="btn" style="left:930px;top:2850px">詳細を見る</span>

<!-- lingual -->
<h3 class="heading" style="top:3140px;font-size:26px">裏側矯正</h3>
<p class="heading" style="top:3190px;font-size:17px;line-height:1.6;color:#5db5ec">歯の裏側に装置を付けるので正面から<br>見えにくい矯正方法です</p>
<p class="abs body-text" style="left:100px;top:3310px;width:440px">花輪町クリア矯正歯科では、クリアフィット矯正と裏側矯正を組み合わせることで、より幅広い歯並びのお悩みに対応しています。見た目に配慮しながら、患者さま一人ひとりに合った治療計画をご提案します。デジタルスキャナーによる簡易シミュレーションで、治療後のイメージも事前にご確認いただけます。</p>
<div class="abs" role="img" aria-label="透明なマウスピース型矯正装置の写真" style="left:600px;top:3240px;width:460px;height:330px;background:linear-gradient(135deg,#eef2f5,#c9d4dd)"></div>

<!-- flow -->
<svg class="abs" style="left:540px;top:3880px" width="120" height="120" viewBox="0 0 120 120"><circle cx="60" cy="60" r="56" fill="none" stroke="#1e9be6" stroke-width="5"/><path d="M60 88 L34 62 a14 14 0 0 1 26-18 a14 14 0 0 1 26 18z" fill="none" stroke="#1e9be6" stroke-width="5" stroke-linejoin="round"/></svg>
<h2 class="heading" style="top:4030px;font-size:38px;font-weight:900">診療の流れ</h2>
<p class="heading" style="top:4090px;font-size:15px;color:#5db5ec;letter-spacing:2px">ご予約から治療開始までの流れをご紹介します</p>
<div class="flow">
  <div class="step"><svg width="36" height="36" viewBox="0 0 36 36"><circle cx="18" cy="18" r="15" fill="none" stroke="#1e9be6" stroke-width="2"/></svg><h4>STEP1</h4><p>ご予約<br>お電話で受付</p></div>
  <div class="step"><svg width="36" height="36" viewBox="0 0 36 36"><path d="M18 30 L6 18 a7 7 0 0 1 12-9 a7 7 0 0 1 12 9z" fill="none" stroke="#1e9be6" stroke-width="2"/></svg><h4>STEP2</h4><p>無料相談<br>お悩みを伺います</p></div>
  <div class="step"><svg width="36" height="36" viewBox="0 0 36 36"><rect x="6" y="6" width="24" height="24" rx="4" fill="none" stroke="#1e9be6" stroke-width="2"/></svg><h4>STEP3</h4><p>精密検査<br>3Dスキャン</p></div>
  <div class="step"><svg width="36" height="36" viewBox="0 0 36 36"><path d="M8 18 l7 7 13-14" fill="none" stroke="#1e9be6" stroke-width="3"/></svg><h4>STEP4</h4><p>治療開始<br>装置をお渡し</p></div>
</div>

<!-- footer -->
<footer class="footer">
  <div class="abs" style="left:40px;top:70px;display:flex;align-items:center;gap:10px"><span style="width:30px;height:30px;border-radius:50%;background:#fff;display:block"></span><strong style="font-size:17px">花輪町クリア矯正歯科</strong></div>
  <div class="abs" style="left:380px;top:50px;font-size:11px;line-height:1.8;opacity:.9">東京都中央区<br>花輪町1-2-3<br>03-0000-0000</div>
  <div class="abs" style="right:40px;top:120px;font-size:10px;opacity:.9">© 2018 花輪町クリア矯正歯科 All rights reserved.</div>
</footer>

</body>
</html>
```